3D Printing Business coming soon page

Hi we are looking for a one page "coming soon" website for our business. The business is called "Solevia Labs" and it is a new solution which 3D Prints Orthotics (Insoles).

The design should include our logo, an improved version of our promotional image (attached), a web form for capturing interest from people, a countdown timer and some text.

Follow the colour scheme which is shown in our logo along with our other colours - Orange (RGB#ff8300) and Light Green (RGB#30f20a)
Updates

Industry/Entity Type

Business

Font styles to use
Sans Serif

Requirements
Must have
• Logo (Attached)
Improved version of Promotional Image
Web Form design for capturing Name, EMail Address and Comments along with a Turin test
Countdown Timer
Text - "Solevia Labs will shake up the Orthotics Industry. Foot Orthosis patient-ready in hours for a fraction of the price you are paying today. Welcome to the new world of 3D Printing!"

```html
<!DOCTYPE html>
<html lang="en">
<head>
<meta charset="utf-8">
<title>Solevia Labs – Coming Soon</title>
<link href="https://fonts.googleapis.com/css2?family=Josefin+Sans:wght@400;600;700&family=Lato:wght@400;700&family=Gochi+Hand&display=swap" rel="stylesheet">
<style>
:root{
  --sky-top:#22a6dc;
  --sky-bottom:#0c6da6;
  --band:#2b86b6;
  --white:#ffffff;
  --ink:#1b1b1b;
  --panel-dark:#262626;
  --panel-light:#6cc4f0;
  --orange:#ff8300;
  --orange-soft:#ffb35c;
  --green:#1e9a44;
  --lime:#a7d63a;
  --yellow:#f1ee6a;
  --captcha:#a32b2b;
  --blue-text:#2a9fd6;
}
*{box-sizing:border-box;margin:0;padding:0}
html,body{width:1200px;height:1184px;overflow:hidden}
body{position:relative;background:linear-gradient(180deg,var(--sky-top) 0%,var(--sky-bottom) 73%);font-family:"Lato",sans-serif;color:var(--white)}
.lower-band{position:absolute;left:0;top:870px;width:1200px;height:314px;background:linear-gradient(180deg,#3a8fba 0%,#1f6f9f 100%)}
.brand-badge{position:absolute;left:30px;top:30px;width:236px;height:236px;border-radius:50%;background:var(--white);display:flex;align-items:center;justify-content:center;text-align:center;font-family:"Josefin Sans",sans-serif;font-weight:700;font-size:38px;line-height:1.05;color:#1a5a9e}
.headline{position:absolute;left:300px;top:56px;width:430px;text-align:center;font-family:"Josefin Sans",sans-serif;font-weight:700;font-size:58px;letter-spacing:1px}
.process{position:absolute;left:180px;top:200px}
.intro{position:absolute;left:200px;top:760px;width:800px;text-align:center;font-size:24px;line-height:28px}
.signup{position:absolute;left:774px;top:55px;width:384px;height:655px}
.signup-frame{position:absolute;left:0;top:25px;width:384px;height:596px;border-radius:18px;background:var(--panel-light)}
.signup-card{position:absolute;left:15px;top:0;width:353px;height:655px;background:var(--panel-dark)}
.signup-title{height:78px;background:var(--ink);display:flex;align-items:center;justify-content:center;font-family:"Josefin Sans",sans-serif;font-weight:700;font-size:33px}
.signup-lede{height:99px;background:var(--panel-light);color:var(--ink);font-family:"Josefin Sans",sans-serif;font-size:17px;line-height:24px;text-align:center;padding:16px 8px 0}
.field{position:absolute;left:14px;width:325px;background:var(--white);border:2px solid #cfcfcf;border-radius:3px;color:#8a8a8a;font-size:16px;padding:12px}
.field-name{top:193px;height:45px}
.field-email{top:250px;height:45px}
.field-comments{top:307px;height:100px}
.captcha{position:absolute;left:14px;top:419px;width:325px;height:130px;background:var(--captcha);border-radius:3px}
.captcha-word{position:absolute;left:6px;top:6px;width:313px;height:62px;background:var(--white)}
.captcha-input{position:absolute;left:6px;top:74px;width:176px;height:50px;background:#f4ec9c;border-radius:2px;font-size:9px;color:#333;padding:8px 0 0 24px}
.captcha-input span{display:block;margin-top:3px;width:146px;height:22px;background:var(--white);border:1px solid #bbb}
.captcha-tools{position:absolute;left:190px;top:76px;display:flex;flex-direction:column;gap:3px}
.captcha-tools i{display:block;width:20px;height:14px;background:#c14646;border-radius:2px}
.captcha-brand{position:absolute;left:224px;top:82px;font-size:11px;line-height:11px;color:#f3dada}
.captcha-brand small{font-size:7px;display:block;margin-top:4px}
.subscribe{position:absolute;left:197px;top:570px;width:142px;height:42px;border-radius:4px;background:linear-gradient(180deg,#ffa030,var(--orange));font-family:"Josefin Sans",sans-serif;font-weight:700;font-size:19px;color:var(--white);padding:12px 0 0 10px}
.subscribe::after{content:"";position:absolute;right:4px;top:4px;width:30px;height:34px;background:#3a3a3a;clip-path:polygon(35% 15%,85% 50%,35% 85%,25% 75%,60% 50%,25% 25%)}
.countdown-title{position:absolute;left:255px;top:896px;font-family:"Josefin Sans",sans-serif;font-weight:700;font-size:42px}
.timer{position:absolute;top:954px;width:134px;height:134px;border-radius:50%;background:var(--orange);border:6px solid var(--orange-soft);display:flex;align-items:center;justify-content:center}
.timer-face{width:110px;height:110px;border-radius:50%;background:var(--white);display:flex;flex-direction:column;align-items:center;justify-content:center;color:var(--blue-text);font-family:"Josefin Sans",sans-serif}
.timer-face b{font-size:46px;line-height:44px}
.timer-face span{font-size:17px;font-weight:600}
.t1{left:257px}.t2{left:446px}.t3{left:634px}.t4{left:821px}
.hand-note{position:absolute;font-family:"Gochi Hand",sans-serif;font-size:24px}
.note-launch{left:35px;top:1106px}
.note-check{left:697px;top:1130px}
.social{position:absolute;top:1106px;width:38px;height:38px;border-radius:50%;background:#1f5da0;border:2px solid var(--white);font-size:9px;font-weight:700;display:flex;align-items:center;justify-content:center}
.s1{left:559px}.s2{left:609px;background:#29a7e1}
.copyright{position:absolute;left:0;top:1161px;width:1200px;text-align:center;font-size:13px}
.doodles{position:absolute;left:0;top:0}
</style>
</head>
<body>
<div class="lower-band"></div>

<div class="brand-badge">Solevia<br>Labs</div>
<h1 class="headline">COMING SOON!</h1>

<svg class="process" width="560" height="560" viewBox="180 200 560 560">
  <defs>
    <linearGradient id="g-yellow" x1="0" y1="0" x2="0" y2="1"><stop offset="0" stop-color="#ffffff"/><stop offset="1" stop-color="var(--yellow)"/></linearGradient>
    <linearGradient id="g-lime" x1="1" y1="0" x2="0" y2="0"><stop offset="0" stop-color="#d8ec5a"/><stop offset="1" stop-color="var(--lime)"/></linearGradient>
    <linearGradient id="g-green" x1="0" y1="1" x2="0" y2="0"><stop offset="0" stop-color="#6ec13e"/><stop offset="1" stop-color="var(--green)"/></linearGradient>
  </defs>
  <path d="M600 340 Q670 370 660 440" fill="none" stroke="url(#g-yellow)" stroke-width="40"/>
  <polygon points="620,430 712,430 660,482" fill="var(--yellow)"/>
  <path d="M590 640 Q560 690 490 680" fill="none" stroke="url(#g-lime)" stroke-width="40"/>
  <polygon points="490,640 490,720 436,672" fill="var(--lime)"/>
  <path d="M290 560 Q245 530 245 480" fill="none" stroke="url(#g-green)" stroke-width="40"/>
  <polygon points="200,484 290,484 245,426" fill="var(--green)"/>
  <path d="M300 285 Q330 255 400 265" fill="none" stroke="url(#g-green)" stroke-width="40"/>
  <polygon points="398,222 398,312 456,265" fill="var(--green)"/>
  <g fill="var(--white)" font-family="Lato, sans-serif" font-weight="700" font-size="24">
    <text x="398" y="276">4</text><text x="650" y="462">1</text><text x="462" y="668">2</text><text x="232" y="482">3</text>
    <text x="288" y="256" transform="rotate(-30 300 245)">Fit it</text>
    <text x="628" y="318" transform="rotate(55 640 330)">Scan the foot</text>
    <text x="512" y="722" transform="rotate(-25 560 705)">Design the</text>
    <text x="530" y="746" transform="rotate(-25 575 730)">Orthotic</text>
    <text x="190" y="500" transform="rotate(60 205 515)">3D Print it</text>
  </g>
  <g stroke="#eaeaea" stroke-width="3">
    <circle cx="530" cy="318" r="75" fill="#d9cbb5" role="img" aria-label="Photo of a hand holding a shoe with a custom insole"/>
    <circle cx="637" cy="568" r="75" fill="#dcdfe3" role="img" aria-label="Photo of a tablet fitted with a 3D scanner"/>
    <circle cx="348" cy="618" r="80" fill="#eef0f2" role="img" aria-label="Screenshot of orthotic design software"/>
    <circle cx="263" cy="343" r="73" fill="#e6dfe0" role="img" aria-label="Photo of a desktop 3D printer"/>
  </g>
  <text x="442" y="446" text-anchor="middle" fill="var(--white)" font-family="Lato, sans-serif" font-weight="700" font-size="62">3D</text>
  <text x="450" y="508" text-anchor="middle" fill="var(--white)" font-family="Lato, sans-serif" font-weight="700" font-size="40">SOLEVIA LABS</text>
</svg>

<p class="intro">Solevia Labs will shake up the Orthotics Industry. Foot Orthosis patient-ready in hours for a fraction of the price you are paying today. Welcome to the new world of 3D Printing!</p>

<form class="signup">
  <div class="signup-frame"></div>
  <div class="signup-card">
    <div class="signup-title">Join Us Here!</div>
    <div class="signup-lede">Simply Enter your Information Below To Get A Bunch Of FREE Information And Lots of GREAT Stuffs!</div>
    <div class="field field-name">Your Name</div>
    <div class="field field-email">Enter Email Address</div>
    <div class="field field-comments">Your Comments</div>
    <div class="captcha">
      <div class="captcha-word" role="img" aria-label="Distorted challenge words"></div>
      <div class="captcha-input">Type the two words:<span></span></div>
      <div class="captcha-tools"><i></i><i></i><i></i></div>
      <div class="captcha-brand">HumanCheck<small>no bots here.</small></div>
    </div>
    <div class="subscribe">SUBSCRIBE</div>
  </div>
</form>

<h2 class="countdown-title">We’ll be online in:</h2>
<div class="timer t1"><div class="timer-face"><b>365</b><span>DAYS</span></div></div>
<div class="timer t2"><div class="timer-face"><b>8</b><span>HOURS</span></div></div>
<div class="timer t3"><div class="timer-face"><b>20</b><span>MINUTES</span></div></div>
<div class="timer t4"><div class="timer-face"><b>28</b><span>SECONDS</span></div></div>

<div class="hand-note note-launch">Time to Launch</div>
<div class="hand-note note-check">Check out!</div>
<svg class="doodles" width="1200" height="1184" fill="none" stroke="#ffffff" stroke-width="2">
  <path d="M230 1128 Q265 1125 278 1096"/><path d="M268 1100 L279 1094 L280 1108"/>
  <path d="M708 1132 Q700 1108 655 1110"/><path d="M664 1103 L652 1110 L664 1117"/>
</svg>
<div class="social s1">Linkly</div>
<div class="social s2">Chirpa</div>

<p class="copyright">Copyright 2014, Solevia Labs. All Rights Reserved.</p>
</body>
</html>
```